Lantern Over Maple Book Cover Design

We need:

Ebook and 6x 9 Inch trade paperback book cover (front, back, spine)

Book Title:Lantern Over Maple
Subtitle: Seven Steps Toward Ordering Every Household Matter Before Trouble Arrives Unannounced

For a book written to help any of us gather the information needed to ensure we are set to take care of our loved ones in case of an emergency. Loved ones, a sense of urgency that leads to feeling calm and prepared is needed!

Target Market(s)

Any adult with children, a partner, parents or assets!

Industry/Entity Type

Financial Planning, Health care, Family

Font styles to use
Serif
Sans Serif

Colors
0054AA
0677BA
7BADD7
CADEEF
E8F1F8
FFF300
FFF600
FEFA6F
FFFEC7
FFFEE8
EE7325
F08F49
F5BC92
FAE3D3
FDF4ED
EB3D1F
EC4F4E
F09395
F8D3D4
FCEDEE

```html
<!DOCTYPE html>
<html lang="en">
<head>
<meta charset="utf-8">
<title>Lantern Over Maple — Book Cover</title>
<link href="https://fonts.googleapis.com/css2?family=Anton&family=Montserrat:wght@400;700&family=Playfair+Display:ital@1&display=swap" rel="stylesheet">
<style>
  :root {
    --paper: #ffffff;
    --ink: #000000;
    --signal-red: #d81f26;
    --deep-red: #8f171c;
    --rule: #111111;
  }
  html, body {
    margin: 0;
    padding: 0;
    width: 800px;
    height: 1200px;
    overflow: hidden;
    background: var(--paper);
  }
  .cover {
    position: relative;
    width: 800px;
    height: 1200px;
    background: var(--paper);
  }
  .cover-art {
    position: absolute;
    inset: 0;
    width: 800px;
    height: 1200px;
  }
  .author {
    font-family: "Montserrat", sans-serif;
    font-weight: 400;
    font-size: 42px;
    fill: var(--ink);
  }
  .title-main {
    font-family: "Anton", sans-serif;
    font-size: 224px;
  }
  .title-top { fill: var(--ink); }
  .title-bottom { fill: url(#redSweep); }
  .title-joiner {
    font-family: "Playfair Display", serif;
    font-style: italic;
    font-size: 50px;
    fill: var(--ink);
  }
  .rule { stroke: var(--rule); stroke-width: 2; }
  .subtitle {
    font-family: "Montserrat", sans-serif;
    font-size: 30px;
    fill: var(--ink);
  }
  .subtitle-accent {
    font-weight: 700;
    fill: var(--signal-red);
  }
</style>
</head>
<body>
<main class="cover">
  <svg class="cover-art" viewBox="0 0 800 1200" xmlns="http://www.w3.org/2000/svg">
    <defs>
      <linearGradient id="redSweep" x1="0" y1="0" x2="1" y2="0">
        <stop offset="0" stop-color="#8f171c"/>
        <stop offset="0.5" stop-color="#d81f26"/>
        <stop offset="1" stop-color="#8f171c"/>
      </linearGradient>
      <radialGradient id="beaconGlow" cx="0.5" cy="0.42" r="0.6">
        <stop offset="0" stop-color="#f2553b"/>
        <stop offset="0.55" stop-color="#d81f26"/>
        <stop offset="0.8" stop-color="#5a1214"/>
        <stop offset="1" stop-color="#ffffff"/>
      </radialGradient>
    </defs>

    <text class="author" x="400" y="80" text-anchor="middle" textLength="372" lengthAdjust="spacingAndGlyphs">DELIA MARCHETTI</text>

    <rect class="hero-illustration" role="img" aria-label="Glowing red emergency beacon light on a black base" x="280" y="135" width="240" height="290" rx="40" fill="url(#beaconGlow)"/>

    <text class="title-main title-top" x="107" y="652" textLength="580" lengthAdjust="spacingAndGlyphs">LANTERN</text>

    <line class="rule" x1="115" y1="701" x2="328" y2="701"/>
    <text class="title-joiner" x="400" y="718" text-anchor="middle">Over</text>
    <line class="rule" x1="472" y1="701" x2="686" y2="701"/>

    <text class="title-main title-bottom" x="109" y="972" textLength="573" lengthAdjust="spacingAndGlyphs">MAPLE</text>

    <line class="rule" x1="147" y1="1057" x2="280" y2="1057"/>
    <text class="subtitle" x="400" y="1069" text-anchor="middle" textLength="204" lengthAdjust="spacingAndGlyphs">SEVEN STEPS</text>
    <line class="rule" x1="520" y1="1057" x2="653" y2="1057"/>

    <text class="subtitle subtitle-accent" x="400" y="1104" text-anchor="middle" textLength="573" lengthAdjust="spacingAndGlyphs">TOWARD ORDERING EVERY HOUSEHOLD MATTER</text>
    <text class="subtitle" x="400" y="1139" text-anchor="middle" textLength="402" lengthAdjust="spacingAndGlyphs">BEFORE TROUBLE ARRIVES UNANNOUNCED</text>
  </svg>
</main>
</body>
</html>
```